Corporate-Design für Trainerin
Zielgruppe
Ich bin selbstständig als Trainerin, Coach und Beraterin in allen Themen der Personalentwicklung tätig. Das Training erfolgt vor allem in dem Bereich der Sozialkompetenz. Konflikt,- Zeit, Selbst- und Stressmanagement. Aber auch im Bereich der Kommunikation und das gesunde Führen. Die Zielgruppe ist mittelständige Unternehmen, die keine eigenständige Personalentwicklungsabteilung haben und gerne auf externe Unterstützung zugreifen.
Aufgabenstellung
Für mein Design suche ich etwas, dass mein Person wiederspiegelt. Ich bin naturgebunden, zuverlässig, natürlich, lege Wert auf Ehrlichkeit, Vertrauen, Wertschätzung, Beständigkeit. Ich bin in Schweden geboren und aufgewachsen und lege viel Wert auf Gleichberechtigung. Ich werde die Kunden mit DU ansprechen, wie es in Schweden üblich ist. Meine schwedischen Wurzeln sind mein USP. Die Trainings sollen bei Wunsch mit schwedischer Verpflegung ergänzt werden. Natur, wenig Hektik steht im Vordergrund. Energie tanken. Das Design soll professionell aussehen aber trotzdem herzlich und einladend sein.

```html
<!DOCTYPE html>
<html lang="de">
<head>
<meta charset="utf-8">
<title>Henriette Wendholt – Geschäftsausstattung</title>
<link rel="stylesheet" href="https://fonts.googleapis.com/css2?family=Montserrat:wght@400;500;600;700&display=swap">
<style>
  :root {
    --backdrop: #dfe0e0;
    --brand-blue: #1572b9;
    --paper: #ffffff;
    --ink: #444444;
    --ink-soft: #555555;
    --rule: #555555;
    --faint: #a5a5a5;
  }
  * { margin: 0; padding: 0; box-sizing: border-box; }
  html, body { width: 878px; height: 1200px; overflow: hidden; }
  body {
    position: relative;
    background: var(--backdrop);
    font-family: "Montserrat", sans-serif;
    color: var(--ink);
  }

  .card {
    position: absolute;
    top: 91px;
    width: 353px;
    height: 228px;
    border-radius: 13px;
    box-shadow: 0 6px 16px rgba(0,0,0,.18);
  }
  .card-back { left: 75px; background: var(--brand-blue); }
  .card-front { left: 440px; background: var(--paper); }

  .brand-mark {
    position: absolute;
    display: flex;
    align-items: center;
    white-space: nowrap;
  }
  .brand-dot { flex: none; border-radius: 50%; border-style: solid; }
  .brand-text { display: flex; flex-direction: column; }
  .brand-name { font-weight: 700; letter-spacing: .01em; line-height: 1; }
  .brand-tagline { font-weight: 400; line-height: 1; color: var(--ink-soft); }

  .card-back .brand-mark { left: 50%; top: 50%; transform: translate(-50%, -50%); flex-direction: column; gap: 8px; }
  .card-back .brand-dot { width: 52px; height: 52px; border-width: 4px; border-color: var(--paper); }
  .card-back .brand-name { color: var(--paper); font-size: 10px; }

  .holder { position: absolute; left: 28px; top: 86px; }
  .holder-name { font-size: 13.5px; font-weight: 400; color: var(--ink-soft); letter-spacing: .01em; line-height: 1.1; }
  .holder-role { font-size: 8px; font-weight: 600; color: var(--ink); margin-top: 1px; }
  .contacts { position: absolute; left: 28px; top: 124px; list-style: none; }
  .contacts li { display: flex; align-items: center; height: 12px; font-size: 6px; color: var(--ink-soft); }
  .contacts svg { width: 9px; height: 9px; margin-right: 10px; stroke: var(--ink-soft); fill: none; stroke-width: 1; }
  .card-divider { position: absolute; left: 175px; top: 62px; width: 1px; height: 106px; background: var(--rule); }
  .card-front .brand-mark { left: 263px; top: 84px; transform: translateX(-50%); flex-direction: column; gap: 8px; }
  .card-front .brand-dot { width: 35px; height: 35px; border-width: 3px; border-color: var(--brand-blue); }
  .card-front .brand-text { align-items: center; gap: 3px; }
  .card-front .brand-name { color: var(--ink); font-size: 11px; }
  .card-front .brand-tagline { font-size: 4px; }

  .letterhead {
    position: absolute;
    left: 97px; top: 358px;
    width: 496px; height: 678px;
    background: var(--paper);
    box-shadow: 0 8px 22px rgba(0,0,0,.2);
  }
  .letterhead .brand-mark.header { left: 165px; top: 32px; gap: 10px; }
  .letterhead .header .brand-dot { width: 30px; height: 30px; border-width: 2.5px; border-color: var(--brand-blue); }
  .letterhead .header .brand-text { gap: 2px; }
  .letterhead .header .brand-name { color: var(--ink); font-size: 9px; }
  .letterhead .header .brand-tagline { font-size: 3.2px; padding-left: 1px; }
  .letter-body {
    position: absolute;
    left: 65px; top: 119px; width: 366px;
    font-size: 7.9px; line-height: 10.4px;
    letter-spacing: -.01em;
    text-align: justify; color: var(--ink);
  }
  .letter-body p + p { margin-top: 10.4px; }
  .footer-mark {
    position: absolute; left: 50px; top: 609px;
    width: 34px; height: 34px;
    border-radius: 50%; border: 3px solid var(--faint);
  }

  .signature-lockup { left: 488px; top: 1092px; gap: 23px; }
  .signature-lockup .brand-dot { width: 71px; height: 71px; border-width: 6px; border-color: var(--brand-blue); }
  .signature-lockup .brand-text { gap: 4px; margin-top: -6px; }
  .signature-lockup .brand-name { color: var(--ink); font-size: 20px; }
  .signature-lockup .brand-tagline { font-size: 8.2px; padding-left: 3px; }
</style>
</head>
<body>

  <section class="card card-back" aria-label="Visitenkarte Rückseite">
    <div class="brand-mark">
      <span class="brand-dot"></span>
      <span class="brand-name">HENRIETTE WENDHOLT</span>
    </div>
  </section>

  <section class="card card-front" aria-label="Visitenkarte Vorderseite">
    <div class="holder">
      <p class="holder-name">Henriette Wendholt</p>
      <p class="holder-role">General Manager</p>
    </div>
    <ul class="contacts">
      <li><svg viewBox="0 0 10 10"><rect x="1" y="2.5" width="8" height="5.5"/><path d="M1 2.5 5 5.8 9 2.5"/></svg>admin@company.com</li>
      <li><svg viewBox="0 0 10 10"><circle cx="5" cy="5" r="3.5"/><path d="M1.5 5h7M5 1.5v7"/></svg>www.yourwebsite.com</li>
      <li><svg viewBox="0 0 10 10"><path d="M2 1.5 3.5 1.5 4.3 3.5 3.2 4.4C3.8 5.6 4.6 6.4 5.8 7L6.7 5.9 8.5 6.7 8.5 8.2C5 8.6 1.6 5.2 2 1.5Z"/></svg>(306) 555-0142</li>
    </ul>
    <div class="card-divider"></div>
    <div class="brand-mark">
      <span class="brand-dot"></span>
      <span class="brand-text">
        <span class="brand-name">HENRIETTE WENDHOLT</span>
        <span class="brand-tagline">TRAINING, COACHING, CONSULTING</span>
      </span>
    </div>
  </section>

  <section class="letterhead" aria-label="Briefbogen">
    <div class="brand-mark header">
      <span class="brand-dot"></span>
      <span class="brand-text">
        <span class="brand-name">HENRIETTE WENDHOLT</span>
        <span class="brand-tagline">TRAINING, COACHING, CONSULTING</span>
      </span>
    </div>
    <div class="letter-body">
      <p>Lorem ipsum dolor sit amet, consectetur adipiscing elit, sed do eiusmod tempor incididunt ut labore et dolore magna aliqua. Ut enim ad minim veniam, quis nostrud exercitation ullamco laboris nisi ut aliquip ex ea commodo consequat. Duis aute irure dolor in reprehenderit in voluptate velit esse cillum dolore eu fugiat nulla pariatur. Excepteur sint occaecat cupidatat non proident, sunt in culpa qui officia deserunt mollit anim id est laborum.</p>
      <p>Lorem ipsum dolor sit amet, consectetur adipiscing elit, sed do eiusmod tempor incididunt ut labore et dolore magna aliqua. Ut enim ad minim veniam, quis nostrud exercitation ullamco laboris nisi ut aliquip ex ea commodo consequat. Duis aute irure dolor in reprehenderit in voluptate velit esse cillum dolore eu fugiat nulla pariatur. Excepteur sint occaecat cupidatat non proident, sunt in culpa qui officia deserunt mollit anim id est laborum.Lorem ipsum dolor sit amet, consectetur adipiscing elit, sed do eiusmod tempor incididunt ut labore et dolore magna aliqua. Ut enim ad minim veniam, quis nostrud exercitation ullamco laboris nisi ut aliquip ex ea commodo consequat. Duis aute irure dolor in reprehenderit in voluptate velit esse cillum dolore eu fugiat nulla pariatur. Excepteur sint occaecat cupidatat non proident, sunt in culpa qui officia deserunt mollit anim id est laborum</p>
      <p>Lorem ipsum dolor sit amet, consectetur adipiscing elit, sed do eiusmod tempor incididunt ut labore et dolore magna aliqua. Ut enim ad minim veniam, quis nostrud exercitation ullamco laboris nisi ut aliquip ex ea commodo consequat. Duis aute irure dolor in reprehenderit in voluptate velit esse cillum dolore eu fugiat nulla pariatur. Excepteur sint occaecat cupidatat non proident, sunt in culpa qui officia deserunt mollit anim id est laborum</p>
    </div>
    <span class="footer-mark" aria-hidden="true"></span>
  </section>

  <div class="brand-mark signature-lockup">
    <span class="brand-dot"></span>
    <span class="brand-text">
      <span class="brand-name">HENRIETTE WENDHOLT</span>
      <span class="brand-tagline">TRAINING, COACHING, CONSULTING</span>
    </span>
  </div>

</body>
</html>
```